Northfield Energy Product Distribution Brochure

We are looking to have our current brochure for our customers completely redesigned...the idea is to present the relevant information in an attractive way . Our website is northfieldenergy-example.com where you can find more information about us. We have included a file with a rough idea of the page order and what each should include but feel free to adapt based on design. The example provided is only for context and doesnt have to be maintained. We will be using the brochure both digitally and in print form. As long as it reads easily and is eye catching, the design can be horizontal or vertical.Final deliverable should be indesign file.

"Our Brands" page: should be limited to one page (space being enough) where it has the header for each one (for example diesel generators) space for one or two lines of text and then the corresponding logos for each of the five categories
Updates

For those asking: the "our brands" page should be a single page layout where there is a header with the corresponding section and space for maybe one line of text followed by the two logos for that category. Each of the product pages should be similar in fashion to the one in the document attached: a photo of the product with some white space and space for the text to be included. We will be posting additional examples today

Target Market(s)

We want to present it to customers both digitally and in print so they can see our products

Industry/Entity Type

Power Generation

Font styles to use
Serif

Requirements
Must have
• Eye catching and able to present the information in a presentable fashion. Rest is up to you.
Nice to have
• Should incorporate the colors of our logo but can also add other depending on design

```html
<!DOCTYPE html>
<html lang="en">
<head>
<meta charset="utf-8">
<title>Northfield Energy – Distributor Program Guide</title>
<link href="https://fonts.googleapis.com/css2?family=Montserrat:wght@300;400;600;700;800&display=swap" rel="stylesheet">
<style>
  :root {
    --yellow: #f7d417;
    --yellow-deep: #e9bd00;
    --ink: #1b1b1b;
    --charcoal: #262626;
    --steel: #3a3a3a;
    --paper: #ffffff;
    --mist: #e9e9e9;
    --text: #555555;
    --backdrop: #f4f4f4;
  }
  * { margin: 0; padding: 0; box-sizing: border-box; }
  html, body { width: 900px; height: 1200px; overflow: hidden; }
  body {
    background: var(--backdrop);
    font-family: "Montserrat", Arial, sans-serif;
    position: relative;
  }
  .page {
    position: absolute;
    width: 360px;
    height: 540px;
    overflow: hidden;
    box-shadow: 0 2px 8px rgba(0,0,0,.18);
  }
  .page-label {
    position: absolute;
    width: 360px;
    text-align: center;
    font-size: 12px;
    color: #444;
  }
  .shapes { position: absolute; inset: 0; }

  /* Cover */
  .cover { left: 80px; top: 20px; background: var(--charcoal); }
  .cover-photo {
    position: absolute; left: 0; top: 0; width: 360px; height: 255px;
    background:
      radial-gradient(circle at 30% 40%, rgba(255,170,60,.55), transparent 30%),
      radial-gradient(circle at 75% 30%, rgba(255,200,90,.45), transparent 25%),
      linear-gradient(180deg, #2a3140 0%, #3a3124 55%, #1a1a1a 100%);
  }
  .cover-title {
    position: absolute; left: 32px; top: 282px; color: var(--paper);
    text-transform: uppercase; line-height: 1;
  }
  .cover-title .small { display: block; font-size: 22px; font-weight: 400; letter-spacing: 1px; margin-bottom: 4px; }
  .cover-title .big { display: block; font-size: 48px; font-weight: 700; letter-spacing: 1px; }
  .cover-subtitle {
    position: absolute; left: 32px; top: 380px; color: var(--yellow);
    font-size: 8px; letter-spacing: 1px; text-transform: uppercase; width: 150px; line-height: 1.5;
  }
  .brand {
    position: absolute; display: flex; align-items: center; gap: 8px;
    color: var(--yellow); font-weight: 700; font-size: 13px; letter-spacing: 1.5px; text-transform: uppercase;
  }
  .brand-mark { width: 14px; height: 14px; background: var(--yellow); }
  .cover .brand { left: 32px; top: 448px; }
  .cover-web {
    position: absolute; left: 32px; top: 500px; color: var(--paper);
    font-size: 10px; font-weight: 600; letter-spacing: 1px; text-transform: uppercase;
  }

  /* Index */
  .index { left: 460px; top: 20px; background: var(--paper); }
  .index-city {
    position: absolute; left: 0; top: 280px; width: 360px; height: 260px;
    background: linear-gradient(180deg, #ffffff 0%, #dcdcdc 60%, #c8c8c8 100%);
  }
  .index-heading {
    position: absolute; right: 24px; top: 22px; color: var(--yellow);
    font-size: 40px; font-weight: 800; letter-spacing: 6px;
  }
  .toc-heading {
    position: absolute; left: 0; width: 360px; top: 108px; text-align: center;
    color: var(--yellow-deep); font-size: 20px; font-weight: 300; line-height: 1.1; text-transform: uppercase;
  }
  .toc { position: absolute; left: 52px; top: 170px; width: 256px; list-style: none; }
  .toc li {
    display: flex; justify-content: space-between; align-items: center;
    height: 21px; margin-bottom: 11px; font-size: 8px; color: var(--ink);
  }
  .toc .entry { background: var(--yellow); flex: 0 0 200px; height: 100%; padding-left: 10px; display: flex; align-items: center; }
  .toc .num { flex: 1; text-align: right; font-weight: 600; padding-right: 4px; }

  /* About */
  .about { left: 80px; top: 600px; background: var(--paper); }
  .about-heading {
    position: absolute; left: 24px; top: 26px; color: var(--yellow-deep);
    font-size: 22px; font-weight: 400; text-transform: uppercase;
  }
  .about-heading strong { font-weight: 700; }
  .about-copy { position: absolute; left: 24px; width: 312px; font-size: 7.5px; line-height: 1.55; color: var(--text); }
  .about-copy p + p { margin-top: 6px; }
  .about-copy.upper { top: 66px; }
  .about-copy.lower { top: 418px; }
  .about-photo {
    position: absolute; left: 0; top: 210px; width: 360px; height: 190px;
    background:
      radial-gradient(circle at 50% 70%, rgba(120,170,230,.45), transparent 45%),
      linear-gradient(180deg, #1c2a44 0%, #2b3f63 55%, #0f1726 100%);
  }
  .about-footer {
    position: absolute; right: 24px; bottom: 14px; font-size: 7px; color: var(--ink);
    background: var(--yellow); padding: 4px 8px; font-weight: 600;
  }

  /* Back */
  .back { left: 460px; top: 600px; background: var(--ink); }
  .back .brand { left: 0; width: 360px; justify-content: center; top: 330px; font-size: 15px; }
  .back-contact {
    position: absolute; left: 0; width: 360px; top: 390px; text-align: center;
    color: var(--paper); font-size: 8px; line-height: 1.8;
  }
  .back-contact .company { color: var(--yellow); font-weight: 700; font-size: 9px; letter-spacing: 1px; }
  .back-contact .web { color: var(--yellow); font-weight: 700; letter-spacing: 1px; }
</style>
</head>
<body>

<!-- Cover page -->
<section class="page cover">
  <div class="cover-photo" role="img" aria-label="Photo of an industrial power plant lit up at night"></div>
  <svg class="shapes" viewBox="0 0 360 540" aria-hidden="true">
    <polygon points="0,250 360,250 360,540 0,540" fill="#222"/>
    <polygon points="120,250 360,250 360,420 260,330" fill="#2e2e2e"/>
    <polygon points="0,330 90,250 180,250 0,420" fill="#2b2b2b"/>
    <polygon points="250,235 360,235 360,345" fill="#f7d417"/>
    <polygon points="200,250 250,250 320,320 290,320" fill="#e9bd00"/>
    <polygon points="0,240 60,240 0,290" fill="#f7d417"/>
    <polygon points="280,540 360,460 360,540" fill="#f7d417"/>
    <polygon points="230,540 300,470 320,470 250,540" fill="#e9bd00"/>
  </svg>
  <h1 class="cover-title">
    <span class="small">Distributor</span>
    <span class="small">Program</span>
    <span class="big">Guide</span>
  </h1>
  <p class="cover-subtitle">Products, Services and Partner Benefits</p>
  <div class="brand"><span class="brand-mark"></span>Northfield Energy</div>
  <p class="cover-web">northfieldenergy-example.com</p>
</section>
<p class="page-label" style="left:80px;top:568px;">Cover Page</p>

<!-- Index page -->
<section class="page index">
  <div class="index-city" role="img" aria-label="Faded photo of a city skyline"></div>
  <svg class="shapes" viewBox="0 0 360 540" aria-hidden="true">
    <polygon points="0,0 150,0 90,80 0,80" fill="#f7d417"/>
    <polygon points="150,0 180,0 120,80 90,80" fill="#262626"/>
  </svg>
  <h2 class="index-heading">INDEX</h2>
  <p class="toc-heading">Table of<br>Content</p>
  <ol class="toc">
    <li><span class="entry">About our company</span><span class="num">03</span></li>
    <li><span class="entry">Our mission and values</span><span class="num">04</span></li>
    <li><span class="entry">Distributor program overview</span><span class="num">05</span></li>
    <li><span class="entry">Diesel generators</span><span class="num">06</span></li>
    <li><span class="entry">Gas generators</span><span class="num">07</span></li>
    <li><span class="entry">Transfer switches</span><span class="num">08</span></li>
    <li><span class="entry">Our brands</span><span class="num">09</span></li>
    <li><span class="entry">Service and support</span><span class="num">10</span></li>
    <li><span class="entry">Ordering and pricing</span><span class="num">11</span></li>
    <li><span class="entry">Contact information</span><span class="num">12</span></li>
  </ol>
</section>
<p class="page-label" style="left:460px;top:568px;">Page 1</p>

<!-- About page -->
<section class="page about">
  <h2 class="about-heading">About <strong>our company</strong></h2>
  <div class="about-copy upper">
    <p>Northfield Energy has supplied reliable power generation equipment to businesses, hospitals, farms and municipalities for more than two decades. Our team works side by side with distributors to select, deliver and maintain the right system for every site, from compact standby units to large prime power installations.</p>
    <p>We combine trusted brands with fast delivery, clear pricing and expert technical help, so our partners can offer their customers dependable energy with confidence.</p>
  </div>
  <div class="about-photo" role="img" aria-label="Photo of a city skyline at night"></div>
  <svg class="shapes" viewBox="0 0 360 540" aria-hidden="true">
    <polygon points="0,200 110,200 0,300" fill="#f7d417"/>
    <polygon points="110,200 135,200 30,300 0,300 0,300" fill="#262626"/>
    <polygon points="260,400 360,400 360,320" fill="#f7d417"/>
    <polygon points="0,540 0,500 40,540" fill="#f7d417"/>
  </svg>
  <div class="about-copy lower">
    <p>Every unit we ship is inspected and tested before it leaves our warehouse. Our service network provides installation guidance, preventive maintenance and emergency repairs across the region, keeping your customers powered when it matters most.</p>
  </div>
  <p class="about-footer">northfieldenergy-example.com</p>
</section>
<p class="page-label" style="left:80px;top:1150px;">Page 2</p>

<!-- Back page -->
<section class="page back">
  <svg class="shapes" viewBox="0 0 360 540" aria-hidden="true">
    <polygon points="0,0 360,0 360,120 250,200 0,90" fill="#2a2a2a"/>
    <polygon points="0,0 170,0 60,110 0,110" fill="#f7d417"/>
    <polygon points="170,0 205,0 95,110 60,110" fill="#e9bd00"/>
    <polygon points="260,0 360,0 360,100" fill="#f7d417"/>
    <polygon points="200,60 360,60 360,140 260,240 180,160" fill="#333"/>
    <polygon points="0,540 0,470 120,540" fill="#2a2a2a"/>
  </svg>
  <div class="brand"><span class="brand-mark"></span>Northfield Energy</div>
  <div class="back-contact">
    <p class="company">NORTHFIELD ENERGY LIMITED, INC.</p>
    <p>1420 North Ridge Road, Houston, TX 77001</p>
    <p>Toll Free: (555) 014-2290</p>
    <p>info@northfieldenergy-example.com</p>
    <p class="web">NORTHFIELDENERGY-EXAMPLE.COM</p>
  </div>
</section>
<p class="page-label" style="left:460px;top:1150px;">Back Page</p>

</body>
</html>
```